Prep Meals Flyer

Company Name: Plate Harbor Co

This is a health and fitness related food company.

Recommended Colours:
- Dark Feature: Smoke effect, Black, Gold, White, Grey

Words to use:
- Fresh | Convenient | Delicious | Low Calories
- 'Mobile & Delivery service'
- 'We're here to simplify your life and amplify your health'
- 'Introducing the future of the food industry'
- 'Prices starting from $8.50'
- 'Offering meals for the whole family including a kids range'

Our logo will be attached as well as a couple of other images that can be used

```html
<!DOCTYPE html>
<html lang="en">
<head>
<meta charset="utf-8">
<title>Plate Harbor Co — Prep Meals Flyer</title>
<link rel="stylesheet" href="https://fonts.googleapis.com/css2?family=Graduate&family=Open+Sans:wght@400;700&display=swap">
<style>
  :root {
    --bg: #2a2a2a;
    --bg-deep: #1f1f1f;
    --smoke: rgba(200, 200, 200, 0.16);
    --gold: #d1ab2c;
    --gold-band: #c9a52f;
    --white: #ffffff;
    --ink: #1b1b1b;
    --frame: #0d0d0d;
    --hex-blue: #2f57b8;
    --hex-pink: #e0405c;
    --hex-yellow: #f2d21a;
  }
  * { margin: 0; padding: 0; box-sizing: border-box; }
  html, body { width: 933px; height: 1200px; overflow: hidden; background: var(--bg); }
  .flyer {
    position: relative; width: 933px; height: 1200px; overflow: hidden;
    background: linear-gradient(180deg, var(--bg) 0%, var(--bg-deep) 100%);
    font-family: "Open Sans", Arial, sans-serif; color: var(--white);
  }
  .smoke {
    position: absolute; left: 0; top: 0; width: 520px; height: 760px;
    background:
      radial-gradient(ellipse 220px 140px at 120px 180px, var(--smoke), transparent 70%),
      radial-gradient(ellipse 180px 220px at 90px 430px, var(--smoke), transparent 70%),
      radial-gradient(ellipse 260px 120px at 260px 650px, rgba(200,200,200,0.10), transparent 70%);
  }
  .corner-band { position: absolute; top: 0; right: 0; width: 933px; height: 420px; }
  .corner-name {
    position: absolute; top: 60px; right: 60px; width: 200px;
    font-family: "Graduate", serif; color: var(--ink);
    font-size: 24px; line-height: 1.2; text-align: center; letter-spacing: 3px;
  }
  .brand-title {
    position: absolute; left: 0; top: 66px; width: 810px; text-align: center;
    font-family: "Graduate", serif; color: var(--gold);
  }
  .brand-title .line-top { display: block; font-size: 42px; letter-spacing: 12px; line-height: 1.1; }
  .brand-title .line-main { display: block; font-size: 78px; letter-spacing: 30px; line-height: 1.05; padding-left: 30px; }
  .social-row { position: absolute; left: 268px; top: 224px; width: 320px; height: 86px; }
  .feature-list { list-style: none; }
  .feature {
    position: absolute; display: flex; align-items: center;
    font-size: 28px; line-height: 1; white-space: nowrap;
  }
  .feature::before {
    content: ""; width: 30px; height: 30px; border-radius: 50%;
    background: var(--gold); margin-right: 8px; flex: none;
  }
  .feature.wide::before { margin-right: 4px; }
  .meal-gallery { position: absolute; top: 705px; left: 31px; width: 874px; height: 390px; }
  .meal-photo {
    position: absolute; top: 0; height: 390px;
    border: 6px solid var(--frame);
  }
  .meal-photo.rice-bowls { left: 0; width: 283px;
    background: linear-gradient(160deg, #3c4a2e 0%, #9a6a3a 35%, #e9e6df 55%, #3d5a2a 75%, #5b5b5b 100%); }
  .meal-photo.grill-plates { left: 294px; width: 286px;
    background: linear-gradient(170deg, #c9c9c4 0%, #a2553a 30%, #6b3a2b 50%, #4c7a35 70%, #d9c7b0 100%); }
  .meal-photo.roast-veg { left: 586px; width: 288px;
    background: linear-gradient(150deg, #4a4a4a 0%, #c45232 30%, #d9b27a 50%, #5b7a33 70%, #c33a2a 90%); }
  .tagline {
    position: absolute; left: 0; top: 1106px; width: 933px; text-align: center;
    font-weight: 700; font-size: 39px; white-space: nowrap;
  }
</style>
</head>
<body>
<main class="flyer">
  <div class="smoke" role="img" aria-label="Soft grey smoke drifting over the dark background"></div>

  <svg class="corner-band" viewBox="0 0 933 420" aria-hidden="true">
    <polygon points="563,0 923,0 923,413" fill="var(--gold-band)"/>
  </svg>
  <div class="corner-name">PLATE<br>HARBOR CO</div>

  <h1 class="brand-title">
    <span class="line-top">PLATE HARBOR</span>
    <span class="line-main">CO</span>
  </h1>

  <svg class="social-row" viewBox="0 0 320 86" aria-label="Social media links">
    <polygon points="6,43 26,6 70,6 90,43 70,80 26,80" fill="none" stroke="var(--hex-blue)" stroke-width="5"/>
    <polygon points="113,43 133,6 177,6 197,43 177,80 133,80" fill="none" stroke="var(--hex-pink)" stroke-width="5"/>
    <polygon points="220,43 240,6 284,6 304,43 284,80 240,80" fill="none" stroke="var(--hex-yellow)" stroke-width="5"/>
  </svg>

  <ul class="feature-list">
    <li class="feature" style="left:254px; top:335px;">Mobile &amp; Delivery service</li>
    <li class="feature" style="left:34px; top:407px;">We're here to simplify your life and amplify your health</li>
    <li class="feature" style="left:118px; top:477px;">Introducing the future of the food industry</li>
    <li class="feature" style="left:240px; top:550px;">Prices starting from $8.50</li>
    <li class="feature wide" style="left:30px; top:619px;">Offering meals for the whole family including a kids range</li>
  </ul>

  <section class="meal-gallery">
    <div class="meal-photo rice-bowls" role="img" aria-label="Meal prep containers of grilled chicken, white rice and broccoli"></div>
    <div class="meal-photo grill-plates" role="img" aria-label="Hand holding meal containers with grilled meats, green beans, plantain and sweet potato"></div>
    <div class="meal-photo roast-veg" role="img" aria-label="Meal prep containers of diced chicken with roasted peppers, tomatoes and zucchini"></div>
  </section>

  <p class="tagline">Fresh | Convenient |Delicious | Low Calories</p>
</main>
</body>
</html>
```